Updated Power Point template design

We need an updated Power Point design template. Please see attach business card for branding, would like to incorporate the blue and black corner design aspect some how.

Attached a sample of current PP

Target Market(s)

Corporate Clients

Industry/Entity Type

Electronics

Requirements
Must have
• We require a whole slide deck ( Title side etc )
Nice to have
• Nice amount of white space on slide

```html
<!DOCTYPE html>
<html lang="en">
<head>
<meta charset="utf-8">
<title>Harwick Components – Slide Deck Template</title>
<link rel="stylesheet" href="https://fonts.googleapis.com/css2?family=Open+Sans:wdth,wght@75..100,300..700&display=swap">
<style>
  :root {
    --bg: #8f8f8f;
    --paper: #ffffff;
    --brand-blue: #1a6fbf;
    --ink: #111111;
    --muted: #6b5f4a;
    --swoosh-grey: #e6e6e6;
    --swoosh-blue: #e3eef9;
  }
  * { margin: 0; padding: 0; box-sizing: border-box; }
  html, body { width: 1200px; height: 1200px; overflow: hidden; background: var(--bg); }
  body { font-family: "Open Sans", Arial, sans-serif; }
  .board { position: absolute; left: 0; top: 0; width: 1500px; height: 1500px; transform: scale(0.8); transform-origin: 0 0; }
  .slide { position: absolute; width: 664px; height: 498px; background: var(--paper); overflow: hidden; box-shadow: 6px 8px 10px rgba(0,0,0,.35); }
  .slide--title { left: 72px; top: 190px; }
  .slide--contents { left: 773px; top: 190px; }
  .slide--content { left: 68px; top: 741px; }
  .slide--closing { left: 773px; top: 741px; }
  .swoosh { position: absolute; inset: 0; width: 664px; height: 498px; }
  .slide > *:not(.swoosh) { position: absolute; }
  .brand { color: var(--brand-blue); font-weight: 700; letter-spacing: .01em; white-space: nowrap; }
  .brand--large { right: 42px; top: 78px; font-size: 22px; }
  .brand--small { right: 16px; top: 30px; font-size: 15px; }
  .brand--footer { left: 50px; top: 418px; font-size: 11.5px; }
  .cover-title { left: 143px; top: 370px; font-size: 40px; font-weight: 400; color: var(--brand-blue); }
  .cover-sub { left: 142px; top: 418px; font-size: 19px; font-weight: 700; line-height: 22px; color: var(--ink); width: 470px; }
  .slide-title { left: 77px; top: 78px; font-size: 24px; font-weight: 600; color: var(--brand-blue); }
  .toc { left: 79px; top: 134px; width: 530px; list-style: none; font-stretch: 80%; color: var(--muted); }
  .toc li { display: flex; align-items: baseline; height: 21.6px; font-size: 12px; }
  .toc li.sub { padding-left: 34px; font-size: 10px; }
  .toc .leader { flex: 1; border-bottom: 1px dotted #9a8e78; margin: 0 4px 0 3px; transform: translateY(-3px); }
  .toc .num { width: 44px; text-align: right; }
  .footer-url { top: 478px; width: 664px; left: 0; text-align: center; font-size: 9px; color: var(--brand-blue); }
  .footer-url::before { content: ""; display: inline-block; width: 6px; height: 6px; border: 1.5px solid var(--brand-blue); border-radius: 50%; margin-right: 6px; vertical-align: 0; }
  .content-sub { left: 76px; top: 104px; font-size: 20px; color: var(--ink); letter-spacing: .02em; }
  .columns { left: 74px; top: 136px; width: 557px; display: grid; grid-template-columns: 270px 270px; column-gap: 16px; font-size: 9.4px; line-height: 14.7px; color: var(--ink); text-align: justify; hyphens: auto; }
  .columns p + p { margin-top: 14.7px; }
  .thanks { left: 55px; top: 330px; font-size: 44px; font-weight: 400; color: var(--brand-blue); letter-spacing: .03em; }
  .contact { left: 187px; top: 405px; font-size: 7px; line-height: 11px; color: #333; list-style: none; }
  .contact li { display: flex; align-items: center; gap: 6px; }
  .contact svg { width: 9px; height: 9px; }
</style>
</head>
<body>
<svg width="0" height="0" style="position:absolute">
  <defs>
    <symbol id="swoosh" viewBox="0 0 664 498">
      <ellipse cx="360" cy="180" rx="346" ry="160" fill="var(--swoosh-grey)"/>
      <ellipse cx="405" cy="160" rx="310" ry="155" fill="var(--swoosh-blue)"/>
      <ellipse cx="425" cy="152" rx="305" ry="158" fill="var(--paper)"/>
    </symbol>
  </defs>
</svg>

<main class="board">
  <section class="slide slide--title">
    <svg class="swoosh"><use href="#swoosh"/></svg>
    <div class="brand brand--large">Harwick Components</div>
    <h1 class="cover-title">CLICK TO ADD TITLE</h1>
    <p class="cover-sub">Lorem ipsum dolor sit amet, consectetur adipisicing elit, sed do eiusmod tempor inci-</p>
  </section>

  <section class="slide slide--contents">
    <svg class="swoosh"><use href="#swoosh"/></svg>
    <div class="brand brand--small">Harwick Components</div>
    <h2 class="slide-title">CLICK TO ADD TITLE</h2>
    <ol class="toc">
      <li><span>Lorem Ipsum is simply dummy text</span><span class="leader"></span><span class="num">1</span></li>
      <li class="sub"><span>a) Of the printing and typesetting industry. Lorem Ipsum has been the try's</span><span class="leader"></span><span class="num">2</span></li>
      <li class="sub"><span>b) Standard dummy text ever since the 1500s, when an unknown printer</span><span class="leader"></span><span class="num">2</span></li>
      <li><span>Lorem Ipsum is simply dummy text is the basic dummy text</span><span class="leader"></span><span class="num">3</span></li>
      <li class="sub"><span>make a type specimen book. It has survived not only five centuries</span><span class="leader"></span><span class="num">4</span></li>
      <li class="sub"><span>leap into electronic typesetting, remaining</span><span class="leader"></span><span class="num">5</span></li>
      <li class="sub"><span>larised in the 1960s with the release of Letraset sheets containing</span><span class="leader"></span><span class="num">6</span></li>
      <li><span>Lorem Ipsum is simply dummy text</span><span class="leader"></span><span class="num">7</span></li>
      <li><span>Lorem Ipsum is simply dummy textlorem ipsum is</span><span class="leader"></span><span class="num">7</span></li>
    </ol>
    <p class="footer-url">www.harwickco.com</p>
  </section>

  <section class="slide slide--content">
    <svg class="swoosh" style="opacity:.7"><use href="#swoosh"/></svg>
    <div class="brand brand--small">Harwick Components</div>
    <h2 class="slide-title" style="top:66px">CLICK TO ADD TITLE</h2>
    <p class="content-sub">Lorem ipsum dolor sit amet, consectetur adipisicing</p>
    <div class="columns">
      <div>
        <p>Lorem Ipsum is simply dummy text of the printing and typesetting industry. Lorem Ipsum has been the industry's standard dummy text ever since the 1500s, when an unknown printer took a galley of type and scrambled it to make a type specimen book. It has survived not only five centuries, but also the leap into electronic typesetting, remaining essentially unchanged. It was popularised in the 1960s with the release of Letraset sheets containing Lorem Ipsum passages, and more recently with desktop publishing software like Aldus PageMaker including versions of Lorem Ipsum.</p>
        <p>It is a long established fact that a reader will be distracted by the readable content of a page when looking at its layout. The point of using Lorem Ipsum is that it has a more-or-less normal distribution of letters, as opposed to using 'Content here, content here', making it look like readable English. Many desktop publishing packages and</p>
      </div>
      <div>
        <p>web page editors now use Lorem Ipsum as their default model text, and a search for 'lorem ipsum' will uncover many web sites still in their infancy. Vari</p>
        <p>Contrary to popular belief, Lorem Ipsum is not simply random text. It has roots in a piece of classical Latin literature from 45 BC, making it over 2000 years old. Richard McClintock, a Latin professor at Hampden-Sydney College in Virginia, looked up one of the more obscure Latin words, consectetur, from a Lorem Ipsum passage, and going through the cites of the word in classical literature, discovered the undoubtable source. Lorem Ipsum comes from sections 1.10.32 and 1.10.33 of "de Finibus Bonorum et Malorum" (The Extremes of Good and Evil) by Cicero, written in 45 BC. This book is a treatise on the theory of ethics, very popular during the Renaissance. The first line of Lorem Ipsum, "Lorem ipsum dolor sit amet..", comes from a line in section 1.10.32.</p>
      </div>
    </div>
    <p class="footer-url">www.harwickco.com</p>
  </section>

  <section class="slide slide--closing">
    <svg class="swoosh"><use href="#swoosh"/></svg>
    <h2 class="thanks">Thank You</h2>
    <div class="brand brand--footer">Harwick Components</div>
    <ul class="contact">
      <li><svg viewBox="0 0 10 10"><circle cx="5" cy="5" r="5" fill="var(--brand-blue)"/><path d="M3 2.5l1 0 .6 1.5-.7.6a4 4 0 0 0 1.5 1.5l.6-.7 1.5.6v1a1 1 0 0 1-1 .8A5 5 0 0 1 2.2 3.5a1 1 0 0 1 .8-1z" fill="#fff"/></svg>555.014.2280 ext. 112</li>
      <li><svg viewBox="0 0 10 10"><circle cx="5" cy="5" r="5" fill="var(--brand-blue)"/><rect x="2.5" y="3.3" width="5" height="3.4" fill="#fff"/><path d="M2.5 3.3l2.5 2 2.5-2" stroke="var(--brand-blue)" stroke-width=".6" fill="none"/></svg>mlarsen@harwickco.com</li>
      <li><svg viewBox="0 0 10 10"><circle cx="5" cy="5" r="5" fill="var(--brand-blue)"/><circle cx="5" cy="5" r="2.6" fill="none" stroke="#fff" stroke-width=".8"/></svg>www.harwickco.com</li>
      <li style="margin-top:2px">480 Alder Lane</li>
      <li>Millbrook, PA 17000</li>
    </ul>
  </section>
</main>
</body>
</html>
```